Gardowell - Direct Mail DL flyer design

Create a direct market flyer (d/l size) to compel people to act and visit our website to buy life insurance.

Copy, example images and notes are provided

Target Market(s)

Families with debt who need life insurance

Industry/Entity Type

Insurance

Requirements
Must have
• Our logo
• Colours are Blue C99, M79, Y0, K0 Green C40, M0, Y100, K0
• Copy side 1 is "For the price of a coffee you can ensure you and your family get the right start."
• Copy side 2 is "It doesn't sound like much, but when it comes to life insurance, $1 a day* can make a huge difference if you were to die.
• For the cost of a cup of coffee a day, you can ensure your family will be left with enough to protect the home, pay for ongoing living expenses and fund your children's continued education.
• Your life is important
• Apply today and get 1 month free cover
• Build your tomorrow
• company logo gardowell.com.au make prominant
• *For a monthly premium of $25.33, a 35 year old non-smoking male can obtain $300,000 of term life cover.
• Example for illistration purpose only. The premium cited is current as at February 2016, is based on the factors referred to in the example and subject to underwriting. You should consider whether this product is appropriate for you. Refer to the Product Disclosure Statement, available from gardowell before deciding whether to acquire the product."
• Footer
• Gardowell Pty Ltd
• ABN 47 253 918 604 AFS Licence 729140
Nice to have
• Coffee cup with pods/capsuals around it white background side 1 and coffee ring stain on reverse as watermark
• Trusafe has been awarded - Merrow Ratings - 2014 Kestrel Protection Honours for Term Cover
• Trusafe has been awarded - Merrow Ratings - 2015 Kestrel Protection Honours for Term Cover

```html
<!DOCTYPE html>
<html lang="en">
<head>
<meta charset="utf-8">
<title>Gardowell DL Flyer</title>
<link href="https://fonts.googleapis.com/css2?family=Roboto:wght@300;400;500;700&display=swap" rel="stylesheet">
<style>
  :root {
    --bg: #e6e6e6;
    --paper: #f8f8f8;
    --cyan-light: #8dd5e3;
    --cyan: #3ec3d9;
    --teal: #0aa3b6;
    --teal-deep: #078fa1;
    --brand-blue: #1c3d96;
    --ink: #111111;
    --headline-ink: #1d2b33;
    --white: #ffffff;
    --coffee-dark: #3a2212;
    --coffee-light: #b99a84;
    --stain-light: #eadfd6;
    --stain-mid: #d8c4b4;
  }
  * { margin: 0; padding: 0; box-sizing: border-box; }
  html, body { width: 1200px; height: 997px; overflow: hidden; background: var(--bg); font-family: 'Roboto', sans-serif; color: var(--ink); }
  .canvas { position: relative; width: 1200px; height: 997px; }
  .page { position: absolute; top: 167px; width: 484px; height: 686px; background: var(--paper); overflow: hidden; box-shadow: 0 14px 18px -10px rgba(0,0,0,.25); }
  .page--front { left: 99px; }
  .page--back { left: 617px; width: 483px; }
  .page svg.waves { position: absolute; inset: 0; width: 100%; height: 100%; }

  .headline { position: absolute; left: 153px; top: 33px; font-size: 33px; line-height: 34.5px; color: var(--headline-ink); font-weight: 300; }
  .headline strong { display: block; color: var(--white); font-weight: 700; }

  .cup-image { position: absolute; left: 16px; top: 380px; width: 390px; height: 260px; border-radius: 10px;
    background: linear-gradient(135deg, var(--coffee-light) 0%, var(--coffee-dark) 50%, var(--coffee-light) 100%); }

  .brand { position: absolute; display: flex; align-items: center; color: var(--brand-blue); font-weight: 400; }
  .brand__mark { background: var(--brand-blue); border-radius: 4px; flex: none; }
  .brand--small { left: 288px; top: 629px; gap: 6px; font-size: 16px; }
  .brand--small .brand__mark { width: 22px; height: 22px; }
  .brand__tag { display: block; font-size: 6px; letter-spacing: 2px; text-align: right; }

  .body-copy { position: absolute; left: 21px; top: 73px; width: 400px; font-size: 13px; line-height: 16.2px; font-weight: 300; color: var(--ink); }
  .key-lines { position: absolute; left: 21px; top: 168px; font-size: 13px; line-height: 16.2px; font-weight: 500; }
  .brand--large { left: 46px; top: 245px; gap: 12px; font-size: 36px; line-height: 1; }
  .brand--large .brand__mark { width: 64px; height: 64px; border-radius: 8px; }
  .brand--large .brand__tag { font-size: 12px; letter-spacing: 4px; margin-top: 4px; }
  .offer-note { position: absolute; left: 24px; top: 336px; width: 420px; font-size: 13px; line-height: 16.5px; font-weight: 500; }
  .disclaimer { position: absolute; left: 26px; top: 380px; width: 190px; font-size: 13px; line-height: 16.2px; font-weight: 300; color: var(--ink); }
  .stain-image { position: absolute; left: 229px; top: 384px; width: 214px; height: 191px; border-radius: 8px;
    background: linear-gradient(135deg, var(--stain-light), var(--stain-mid)); }
  .legal { position: absolute; left: 26px; top: 600px; font-size: 13px; line-height: 16.5px; font-weight: 500; }
</style>
</head>
<body>
<main class="canvas">
  <section class="page page--front">
    <svg class="waves" viewBox="0 0 484 686" preserveAspectRatio="none" aria-hidden="true">
      <defs>
        <linearGradient id="bandFront" x1="0" y1="0" x2="1" y2="1">
          <stop offset="0" stop-color="#0b97a8"/>
          <stop offset="1" stop-color="#15bcd6"/>
        </linearGradient>
      </defs>
      <path d="M0 0H484V410C420 420 340 400 250 350C180 310 100 400 0 480Z" fill="var(--cyan-light)"/>
      <path d="M0 0H484V300C440 240 360 200 250 200C150 200 80 150 0 165Z" fill="#86d2e1" opacity=".7"/>
      <path d="M0 165C120 150 230 250 320 320C380 370 440 410 484 405V325C484 380 430 420 360 390C270 350 170 270 0 260Z" fill="url(#bandFront)"/>
      <path d="M0 260C120 250 220 320 300 355C200 320 110 350 0 470Z" fill="#1aa8bd" opacity=".55"/>
    </svg>
    <h1 class="headline">For the price<br>of a coffee<br>you can ensure<strong>you and your family<br>get the right start.</strong></h1>
    <div class="cup-image" role="img" aria-label="Photo: top view of a cup of black coffee with coffee beans scattered around it"></div>
    <div class="brand brand--small">
      <span class="brand__mark"></span>
      <span>gardowell.com.au<span class="brand__tag">build your tomorrow</span></span>
    </div>
  </section>

  <section class="page page--back">
    <svg class="waves" viewBox="0 0 483 686" preserveAspectRatio="none" aria-hidden="true">
      <defs>
        <linearGradient id="bandTop" x1="0" y1="0" x2="1" y2="0">
          <stop offset="0" stop-color="#7ad0df"/>
          <stop offset="1" stop-color="#0aa9bd"/>
        </linearGradient>
      </defs>
      <path d="M0 0H483V6L0 47Z" fill="url(#bandTop)" opacity=".8"/>
      <path d="M150 32L483 5V73Z" fill="var(--teal)"/>
      <path d="M0 686V636L240 662L483 645V686Z" fill="var(--teal)"/>
      <path d="M0 636L240 662L0 670Z" fill="#79cfde"/>
    </svg>
    <p class="body-copy">It doesn't sound like much, but when it comes to life insurance, $1 a day* can make a huge difference if you were to die.<br>For the cost of a cup of coffee a day, you can ensure your family will be left with enough to protect the home, pay for ongoing living expenses and fund your children's continued education.</p>
    <p class="key-lines">Your life is important<br>Apply today and get 1 month free cover<br>Build your tomorrow</p>
    <div class="brand brand--large">
      <span class="brand__mark"></span>
      <span>gardowell.com.au<span class="brand__tag">build your tomorrow</span></span>
    </div>
    <p class="offer-note">*For a monthly premium of $25.33, a 35 year old non-smoking male can obtain $300,000 of term life cover.</p>
    <div class="stain-image" role="img" aria-label="Photo: coffee ring stain used as a faint watermark"></div>
    <p class="disclaimer">Example for illustration purpose only. The premium cited is current as at February 2016, is based on the factors referred to in the example and subject to underwriting. You should consider whether this product is appropriate for you. Refer to the Product Disclosure Statement, available from gardowell before deciding whether to acquire the product."</p>
    <p class="legal">Gardowell Pty Ltd<br>ABN 47 253 918 604 AFS Licence 729140</p>
  </section>
</main>
</body>
</html>
```